Meridian Clearsound Wellness LLC Card Design

Need business card with a logo for a hearing aid sales and audiology business. We have two Hearing Instrument Specialists and one Audiologist on staff. Over 25 years in business. Locally owned and operated. Financing available. Most insurances accepted.

Meridian Clearsound Wellness LLC
48730 W Larkfield, Suite 9
Spokane, WA 99371
509-617-2084
www.meridianclearsound-example.com

Manager
Tobias Wrenfield HIS COHC
License #81957260

Target Market(s)

50yr old + people with a hearing loss.

Industry/Entity Type

Business

Contact Information for Business Card

48730 W Larkfield, Suite 9
Spokane, WA 99371
509-617-2084
www.meridianclearsound-example.com

Manager
Tobias Wrenfield HIS COHC
RTEQ #81957260

Font styles to use
Serif
Sans Serif

Requirements
Must have
• Business name, Tobias's name and title(s) and contact information, License #, web address
Nice to have
Should not have

```html
<!DOCTYPE html>
<html lang="en">
<head>
<meta charset="utf-8">
<title>Meridian Clearsound Wellness LLC – Business Card</title>
<link rel="stylesheet" href="https://fonts.googleapis.com/css2?family=Oswald:wght@600&family=Questrial&display=swap">
<style>
  :root {
    --stage: #141414;
    --brand-blue: #1f4b9e;
    --paper: #ffffff;
    --ink-light: #ffffff;
    --divider: rgba(255,255,255,0.45);
  }
  * { margin: 0; padding: 0; box-sizing: border-box; }
  html, body { width: 1200px; height: 1200px; overflow: hidden; background: var(--stage); }
  .sheet {
    width: 1200px; height: 1200px;
    display: flex; flex-direction: column; align-items: center; justify-content: center; gap: 64px;
  }
  .card {
    position: relative; width: 840px; height: 480px; border-radius: 22px; overflow: hidden;
  }
  .card--front { background: var(--brand-blue); color: var(--ink-light); }
  .card--back { background: var(--paper); display: flex; align-items: center; justify-content: center; }

  .side-mark {
    position: absolute; left: 80px; bottom: 44px; max-height: 400px;
    writing-mode: vertical-rl; transform: rotate(180deg);
    font-family: "Oswald", "Arial Narrow", sans-serif; font-weight: 600;
    font-size: 31px; line-height: 1.12; letter-spacing: 0.3px; text-transform: uppercase;
    white-space: nowrap;
  }
  .accent-bar { position: absolute; background: var(--paper); width: 9px; bottom: 0; }
  .accent-bar--outer { left: 24px; height: 230px; }
  .accent-bar--inner { left: 44px; height: 180px; }

  .identity {
    position: absolute; left: 200px; top: 44px; padding-left: 22px;
    border-left: 1px solid var(--divider);
    font-family: "Questrial", "Century Gothic", sans-serif;
  }
  .identity__name { font-size: 38px; line-height: 1.1; white-space: nowrap; }
  .identity__creds { font-size: 18px; letter-spacing: 1px; margin-left: 6px; }
  .identity__title { font-size: 22px; margin-top: 2px; }

  .contact {
    position: absolute; left: 410px; top: 190px; list-style: none;
    font-family: "Questrial", "Century Gothic", sans-serif; font-size: 20px; line-height: 1.45;
    white-space: nowrap;
  }
  .contact li { display: flex; align-items: flex-start; gap: 12px; }
  .contact svg { width: 16px; height: 16px; margin-top: 6px; flex: none; fill: var(--ink-light); }
  .contact .indent { padding-left: 28px; }

  .license {
    position: absolute; right: 34px; bottom: 28px;
    font-family: "Questrial", "Century Gothic", sans-serif; font-size: 18px;
  }

  .back-mark {
    font-family: "Oswald", "Arial Narrow", sans-serif; font-weight: 600; text-align: center;
    color: var(--brand-blue); font-size: 44px; line-height: 1.1; text-transform: uppercase;
  }
</style>
</head>
<body>
<main class="sheet">
  <section class="card card--front" aria-label="Card front">
    <div class="side-mark">Meridian<br>Clearsound Wellness LLC</div>
    <span class="accent-bar accent-bar--outer"></span>
    <span class="accent-bar accent-bar--inner"></span>

    <div class="identity">
      <p class="identity__name">Tobias Wrenfield<span class="identity__creds">HIS COHC</span></p>
      <p class="identity__title">Manager</p>
    </div>

    <ul class="contact">
      <li><svg viewBox="0 0 24 24" aria-hidden="true"><path d="M6.6 10.8a15 15 0 0 0 6.6 6.6l2.2-2.2a1 1 0 0 1 1-.25 11.4 11.4 0 0 0 3.6.57 1 1 0 0 1 1 1V20a1 1 0 0 1-1 1A17 17 0 0 1 3 4a1 1 0 0 1 1-1h3.5a1 1 0 0 1 1 1c0 1.25.2 2.45.57 3.57a1 1 0 0 1-.25 1z"/></svg>509-617-2084</li>
      <li><svg viewBox="0 0 24 24" aria-hidden="true"><path d="M4 2l16 9-7 2-3 8z"/></svg>www.meridianclearsound-example.com</li>
      <li><svg viewBox="0 0 24 24" aria-hidden="true"><path d="M12 2a7 7 0 0 0-7 7c0 5 7 13 7 13s7-8 7-13a7 7 0 0 0-7-7zm0 9.5A2.5 2.5 0 1 1 12 6.5a2.5 2.5 0 0 1 0 5z"/></svg>48730 W Larkfield, Suite 9</li>
      <li class="indent">Spokane, WA 99371</li>
    </ul>

    <p class="license">License #81957260</p>
  </section>

  <section class="card card--back" aria-label="Card back">
    <p class="back-mark">Meridian<br>Clearsound Wellness LLC</p>
  </section>
</main>
</body>
</html>
```